Business Card Design for Cybersecurity Company - QuorvaNet Systems

We need a business card design for our new cybersecurity company, QuorvaNet. We’re going for a clean, hi tech look that feels modern, premium, and trustworthy. We want a design that really stands out and makes people say WOW when we hand it over!

QuorvaNet delivers reliable IT support and managed services for small and mid sized businesses. We help companies stay secure, efficient, and connected through proactive monitoring, cybersecurity services, cloud management, and remote support.

Target Market(s)

Designers should target small and mid sized businesses that need dependable cybersecurity and IT support.

Industry/Entity Type

Cybersecurity, Managed Service Provider, IT services

Contact Information for Business Card

Contact information

Requirements
Must have
• The card should look clean, modern, and tech focused, with the QuorvaNet logo, clear contact info, and strong readability. It needs to feel premium and professional while still keeping a simple layout that fits a cybersecurity and IT brand.
Nice to have
• Nice to have elements include subtle touches that give the card a modern, tech feel, along with a layout that works well in different background styles.
Should not have
• The card should avoid clutter, loud graphics, or anything that takes attention away from the logo and contact details.

```html
<!DOCTYPE html>
<html lang="en">
<head>
<meta charset="utf-8">
<title>QuorvaNet Systems – Business Card</title>
<link rel="stylesheet" href="https://fonts.googleapis.com/css2?family=Montserrat:wght@400;600&family=Questrial&display=swap">
<style>
  :root {
    --bg: #000000;
    --card-white: #ffffff;
    --ink: #1c1c24;
    --purple: #6a45a8;
    --blue: #4466b3;
    --violet: #6f4aa3;
    --faint: #d5d3ea;
    --muted: #3a3a48;
  }
  * { margin: 0; padding: 0; box-sizing: border-box; }
  html, body {
    width: 805px; height: 1200px; overflow: hidden;
    background: var(--bg);
  }
  .canvas {
    position: relative; width: 805px; height: 1200px;
  }
  .card {
    position: absolute; left: 102px; width: 600px; height: 342px; overflow: hidden;
  }
  .card--front { top: 200px; background: var(--card-white); }
  .card--back {
    top: 640px;
    background: linear-gradient(90deg, var(--blue) 0%, var(--violet) 70%, #71479f 100%);
  }

  .brand {
    position: absolute; display: flex; align-items: center; gap: 14px;
    font-family: "Montserrat", sans-serif; font-weight: 600;
  }
  .brand__dot { border-radius: 50%; flex: none; }
  .card--front .brand { left: 36px; top: 42px; color: var(--purple); font-size: 36px; }
  .card--front .brand__dot { width: 58px; height: 58px; background: var(--purple); }
  .card--back .brand {
    left: 50%; top: 50%; transform: translate(-50%, -50%);
    color: var(--card-white); font-size: 40px; white-space: nowrap;
  }
  .card--back .brand__dot { width: 66px; height: 66px; border: 3px solid var(--card-white); }

  .holder {
    position: absolute; left: 38px; top: 154px; padding-left: 14px;
    border-left: 4px solid var(--purple);
  }
  .holder__name {
    font-family: "Montserrat", sans-serif; font-weight: 600; font-size: 23px;
    color: var(--purple); letter-spacing: 0.2px; line-height: 1.1;
  }
  .holder__role {
    font-family: "Montserrat", sans-serif; font-weight: 600; font-size: 6.5px;
    letter-spacing: 1px; color: var(--muted); text-transform: uppercase; margin-top: 3px;
  }

  .contacts {
    position: absolute; left: 34px; top: 222px; list-style: none;
    font-family: "Questrial", sans-serif; font-size: 16.5px; color: var(--ink);
  }
  .contacts li { display: flex; align-items: center; gap: 9px; height: 25px; }
  .contacts svg { width: 16px; height: 16px; flex: none; }
  .contacts .accent { color: var(--purple); }

  .decor {
    position: absolute; right: -30px; top: 110px; width: 270px; height: 270px;
    border-radius: 50%;
    background: radial-gradient(circle, rgba(213,211,234,0.65) 0%, rgba(213,211,234,0.35) 55%, rgba(213,211,234,0) 72%);
  }
</style>
</head>
<body>
<main class="canvas">
  <section class="card card--front" aria-label="Card front">
    <div class="brand"><span class="brand__dot"></span><span class="brand__name">QuorvaNet</span></div>

    <div class="holder">
      <h1 class="holder__name">DANA HOLLOWAY</h1>
      <p class="holder__role">Owner | CEO | QuorvaNet Systems</p>
    </div>

    <ul class="contacts">
      <li>
        <svg viewBox="0 0 16 16" aria-hidden="true"><path fill="#6a45a8" d="M3.5 1.5l2.3 2.8-1.3 1.6c.9 2 2.4 3.6 4.5 4.6l1.6-1.3 2.9 2.2-1.3 2.4C7 13.600 2.4 9 1.200 3z"/></svg>
        (855) 300-QNET
      </li>
      <li>
        <svg viewBox="0 0 16 16" aria-hidden="true"><rect x="4" y="1" width="8" height="14" rx="1.5" fill="none" stroke="#6a45a8" stroke-width="1.6"/><circle cx="8" cy="12.4" r="0.9" fill="#6a45a8"/></svg>
        (555) 014-2287
      </li>
      <li>
        <svg viewBox="0 0 16 16" aria-hidden="true"><rect x="1" y="3.5" width="14" height="9" fill="#6a45a8"/><path d="M1.5 4l6.5 5 6.5-5M1.5 12l5-4M14.5 12l-5-4" fill="none" stroke="#fff" stroke-width="1"/></svg>
        dana@<span class="accent">quorvanet</span>.com
      </li>
      <li>
        <svg viewBox="0 0 16 16" aria-hidden="true"><g fill="none" stroke="#6a45a8" stroke-width="1.2"><circle cx="8" cy="8" r="6.5"/><ellipse cx="8" cy="8" rx="3" ry="6.5"/><path d="M1.5 8h13M2.5 4.8h11M2.5 11.2h11"/></g></svg>
        www.<span class="accent">quorvanet</span>.com
      </li>
    </ul>

    <div class="decor" role="img" aria-label="Faint large brand mark decoration"></div>
  </section>

  <section class="card card--back" aria-label="Card back">
    <div class="brand"><span class="brand__dot"></span><span class="brand__name">QuorvaNet Systems</span></div>
  </section>
</main>
</body>
</html>
```